Verdane Clinical Spa needs an eye-catching poster to help promote our largest sale of spring!

We need a poster that will go on the back of the doors in the patient rooms. Our medical spa is professional and high-end, so we want the poster to look sophisticated, yet very eye-catching.
This project is for our Marigold Jubilee special, our second largest sale of the year.

Name: Marigold Jubilee
Slogan: Let Your Beauty Bloom
Sale: The More You Buy, The More You Save

Choose from your favorite spa services
NEVRIL, Laser Treatments, Microderms, and More!

It would be great to have something blooming. Flowers, or somehow make a woman look like she's blooming.

I am attaching a visual description of our special. However, the poster should NOT include the pricing tiers. I am also attaching our business logo. Thank you!!

Target Market(s)

A majority are women, but some are men. Around 25-55 in age. Middle to upper class who are likely to spend more money.

Industry/Entity Type

Medical

Font styles to use
Sans Serif
Script

Colors

Designer to choose colors to be used in the design.

Requirements
Must have
• Name of promotion: Marigold Jubilee
• Slogan: "Let Your Beauty Bloom"
• Concept "The more you buy, the more you save on your favorite spa services"
• Select from your favorite spa services such as NEVRIL, laser treatments, microderms, and more!
• Website: VerdaneSpaDeals.com
• Our logo (attached)
Nice to have
• Modern and creative design. Somehow tying in the "Let your beauty bloom" theme. We don't want the focus to be "The more you buy the more you save"
• We are looking for a unique design that is unlike traditional medical spas in the area that typically include a lot of white and a lot of overly photoshopped images.
• Creativity is key! Something that's different than just text and images. We would be so excited to see that!
Should not have
• Not too much text, but enough to get the point across.

```html
<!DOCTYPE html>
<html lang="en">
<head>
<meta charset="utf-8">
<title>Verdane Clinical Spa – Marigold Jubilee Poster</title>
<link rel="stylesheet" href="https://fonts.googleapis.com/css2?family=Playfair+Display:wght@700;900&family=Kaushan+Script&family=Lato:wght@700&family=Libre+Baskerville:wght@400;700&display=swap">
<style>
  :root {
    --stage: #b3a498;
    --paper: #ffffff;
    --pink-light: #f6d3ea;
    --pink-mid: #e6a3cf;
    --pink-deep: #c86aa8;
    --blossom: #e48fc4;
    --blossom-light: #f8dcee;
    --magenta: #e0147f;
    --plum: #8a1f5e;
    --blue: #1a6fb3;
    --ink: #1d1d1b;
    --black: #111111;
    --brand-dot: #9ccf7a;
  }
  * { margin: 0; padding: 0; box-sizing: border-box; }
  html, body { width: 1200px; height: 900px; overflow: hidden; }
  body { background: var(--stage); position: relative; }

  .poster {
    position: absolute;
    left: 300px; top: 31px;
    width: 600px; height: 838px;
    background: var(--paper);
    padding: 8px;
    box-shadow: 0 4px 14px rgba(0,0,0,0.25);
  }
  .poster__inner {
    position: relative;
    width: 100%; height: 100%;
    overflow: hidden;
  }
  .poster__photo {
    position: absolute; inset: 0;
    background:
      radial-gradient(ellipse 40% 34% at 72% 36%, #f3d9d3 0%, rgba(243,217,211,0) 100%),
      linear-gradient(180deg, var(--pink-light) 0%, var(--pink-mid) 62%, var(--pink-deep) 100%);
  }
  .poster__blossoms {
    position: absolute;
    right: -30px; top: -30px;
    width: 270px; height: 220px;
    border-radius: 50%;
    background: radial-gradient(ellipse at 55% 45%, var(--blossom-light) 0%, var(--blossom) 45%, rgba(228,143,196,0) 75%);
  }

  .brand {
    position: absolute;
    left: 28px; top: 0;
    width: 300px; height: 122px;
    background: var(--paper);
    border-radius: 0 0 10px 10px;
    display: flex; align-items: center; justify-content: center; gap: 10px;
  }
  .brand__dot { width: 20px; height: 20px; border-radius: 50%; background: var(--brand-dot); flex: none; }
  .brand__name {
    font-family: "Libre Baskerville", serif;
    font-weight: 400;
    font-size: 22px;
    color: var(--ink);
    white-space: nowrap;
  }

  .services {
    position: absolute;
    left: 30px; top: 150px;
    width: 250px;
    font-family: "Lato", sans-serif;
    font-weight: 700;
    font-size: 16px;
    line-height: 1.4;
    color: var(--plum);
  }

  .promo-title {
    position: absolute;
    left: 28px; top: 335px;
    font-family: "Playfair Display", serif;
    font-weight: 900;
    font-size: 70px;
    line-height: 0.98;
    color: var(--magenta);
    text-transform: uppercase;
    letter-spacing: -1px;
    text-shadow: 2px 2px 4px rgba(90,0,50,0.35);
    white-space: nowrap;
  }

  .slogan {
    position: absolute;
    left: 36px; top: 538px;
    font-family: "Kaushan Script", cursive;
    font-size: 46px;
    color: var(--blue);
    transform: rotate(-8deg);
    transform-origin: left center;
    white-space: nowrap;
  }

  .dates {
    position: absolute;
    left: 0; top: 630px;
    width: 350px; height: 56px;
    background: linear-gradient(90deg, var(--black) 0%, var(--black) 70%, rgba(17,17,17,0.6) 100%);
    display: flex; align-items: center;
    padding-left: 30px;
    font-family: "Libre Baskerville", serif;
    font-weight: 700;
    font-size: 27px;
    color: var(--paper);
    white-space: nowrap;
  }

  .deal-badge {
    position: absolute;
    left: 376px; top: 576px;
    width: 190px; height: 190px;
  }
  .deal-badge__text {
    position: absolute; inset: 0;
    display: flex; flex-direction: column; align-items: center; justify-content: center;
    transform: rotate(-15deg);
    font-family: "Libre Baskerville", serif;
    font-size: 17px;
    line-height: 1.1;
    color: var(--paper);
    text-transform: uppercase;
    letter-spacing: 1px;
    white-space: nowrap;
  }
  .deal-badge__text strong { font-size: 21px; }

  .web-band {
    position: absolute;
    left: 6px; right: 6px; top: 775px;
    height: 47px;
    background: var(--magenta);
    display: flex; align-items: center;
    padding-left: 14px;
    font-family: "Libre Baskerville", serif;
    font-weight: 700;
    font-size: 21px;
    letter-spacing: 1.5px;
    color: var(--paper);
  }
</style>
</head>
<body>
  <div class="poster">
    <div class="poster__inner">
      <div class="poster__photo" role="img" aria-label="Soft pink portrait photo of a smiling young woman"></div>
      <div class="poster__blossoms" role="img" aria-label="Pink magnolia blossoms blooming in the woman's hair"></div>

      <div class="brand">
        <span class="brand__dot"></span>
        <span class="brand__name">Verdane Clinical Spa</span>
      </div>

      <p class="services">Choose from your favorite spa services: NEVRIL, laser treatments, microderms &amp; more!</p>

      <h1 class="promo-title">Marigold<br>Jubilee</h1>

      <p class="slogan">let your beauty bloom</p>

      <div class="dates">April 20 - June 2</div>

      <div class="deal-badge">
        <svg width="190" height="190" viewBox="0 0 190 190" aria-hidden="true">
          <polygon fill="#1a6fb3" points="95,5 106,23 124,10 129,31 150,25 148,47 169,48 159,67 179,76 163,90 179,104 160,113 171,132 150,134 153,155 132,151 126,172 109,160 95,180 81,160 64,172 58,151 37,155 40,134 19,132 30,113 11,104 27,90 11,76 31,67 21,48 42,47 40,25 61,31 66,10 84,23"/>
        </svg>
        <div class="deal-badge__text">
          <span>The more</span>
          <span>you <strong>buy</strong></span>
          <span>the more</span>
          <span>you <strong>save</strong></span>
        </div>
      </div>

      <div class="web-band">VerdaneSpaDeals.com</div>
    </div>
  </div>
</body>
</html>
```